Cyber Security firm requires new branding and website design

We are open to advice on project budget so feel free to message me regarding this. We understand there are people from all over the world looking at this so initially we may be looking at just a landing page to just give us an idea of the design and that can be enough to win this contest. From there we can agree a reward / payment for the whole site.
We're looking for a Designer with UI/UX and some branding skills. We really need someone to give us a direction and then create a mock-up in Photoshop. We have a great logo and so far our website has done the job but is very basic www.velquant.com . We can reuse most the content (and this can be used by the Designer) but we need a complete redesign. Keep it clear, simple, classy and uncluttered and we certainly need new color scheme.
I have attached our logo's and a copy of our business cards (the black logo is actually silver foil) to give you an idea of the sort of branding we like.
We are based in Los Angeles and our clients range from the Entertainment business and start-ups to Law and Financial firms so we need a site design that appeals to all of these sectors.
Once we have the design we can give it to our developer to turn into a working site.
Updates
I wasn't sure how this worked as its the first time I have used the site.
Happy to take feedback on what would be most attractive to you guys to get you to want to design for us.
Cheers
Dale
The styles we like personally tend to have blocks of content and some funky HTML 5 stuff (If you can design it we can code it). Here are some examples:
http://www.plumbo.co
http://quenlarfitnesshall.com/
http://grovemarkstudio.com/
We are a fun company and have a good sense of humor. Our client generally do too but they are also dealing with serious issues so if you can get something that's fun but puts across that we are serious about what we do that would be great. Oh and we love this one so if you can take some influence from this but keep it professional we would love to see it:
http://brightkettleworks.com/
I also like the old typewriter style lettering i have seen used on contact forms. However this has to be a cohesive design so we want you to add what looks right not just everything we like (unless you can do that well).
We understand that you show a static site so this is hard to demonstrate but we particularly like the videos people are embedding nowadays and would love to avoid stock photos where we can:
https://www.coinvanta.com/home
Hopefully this gives you all more food for thought.
Industry/Entity Type
Business
Colors
Designer to choose colors to be used in the design.
Look and feel
Each slider illustrates characteristics of the customer's brand and the style your logo design should communicate.

```html
<!DOCTYPE html>
<html lang="en">
<head>
<meta charset="utf-8">
<title>Velquant Security – Landing Page</title>
<link rel="stylesheet" href="https://fonts.googleapis.com/css2?family=Quicksand:wght@400;500;700&family=Mulish:wght@300;400&display=swap">
<style>
  :root {
    --navy: #1c2e3d;
    --navy-deep: #172735;
    --paper: #e8e8e8;
    --header: #eeeeee;
    --teal: #1ab5a3;
    --white: #ffffff;
    --ink: #3b4650;
    --muted: #8c98a3;
    --dash: #50606d;
  }
  * { box-sizing: border-box; margin: 0; padding: 0; }
  html, body { width: 1200px; height: 789px; overflow: hidden; background: var(--paper); }
  body { position: relative; font-family: "Mulish", sans-serif; color: var(--ink); }

  .site-header {
    position: absolute; left: 0; top: 0; width: 1200px; height: 84px;
    background: var(--header); z-index: 3;
  }
  .brand {
    position: absolute; left: 150px; top: 26px;
    display: flex; align-items: center; gap: 10px;
  }
  .brand-mark { width: 28px; height: 28px; background: var(--ink); }
  .brand-name {
    font-family: "Quicksand", sans-serif; font-weight: 700; font-size: 20px;
    letter-spacing: 2px; text-transform: uppercase; color: var(--ink); line-height: 1;
  }
  .main-nav {
    position: absolute; left: 470px; top: 34px;
    display: flex; gap: 28px; list-style: none;
    font-family: "Quicksand", sans-serif; font-size: 13px; font-weight: 500; color: var(--ink);
  }
  .main-nav .is-active { color: var(--teal); }

  .edge { position: absolute; left: 0; width: 1200px; height: 10px; z-index: 2; }

  .hero-top {
    position: absolute; left: 0; top: 84px; width: 1200px; height: 220px;
    background: var(--navy);
  }
  .hero-band { position: absolute; left: 0; top: 304px; width: 1200px; height: 120px; background: var(--paper); }
  .hero-bottom {
    position: absolute; left: 0; top: 424px; width: 1200px; height: 120px;
    background: var(--navy);
  }
  .hero-bottom .rule {
    position: absolute; left: 60px; right: 60px; top: 92px; border-top: 1px dashed var(--dash);
  }

  .slide-card {
    position: absolute; left: 340px; top: 140px; width: 520px; height: 320px;
    background: var(--navy); border: 6px solid var(--white);
    box-shadow: 0 10px 30px rgba(0,0,0,0.35); z-index: 4;
    padding: 64px 48px 0;
  }
  .slide-title {
    font-family: "Quicksand", sans-serif; font-weight: 400; font-size: 25px;
    color: var(--teal); line-height: 1.2;
  }
  .slide-divider { width: 140px; border-top: 1px solid var(--teal); margin: 14px 0 16px; }
  .slide-text { font-size: 13px; line-height: 1.6; color: var(--muted); max-width: 300px; }
  .btn-contact {
    display: inline-block; margin-top: 22px; padding: 8px 14px;
    background: var(--teal); color: var(--white);
    font-family: "Quicksand", sans-serif; font-size: 11px; font-weight: 700;
  }
  .slide-arrow {
    position: absolute; top: 270px; width: 44px; height: 44px; border-radius: 50%;
    background: var(--white); z-index: 5; display: flex; align-items: center; justify-content: center;
  }
  .slide-arrow.prev { left: 318px; }
  .slide-arrow.next { left: 838px; }
  .slide-dots { position: absolute; left: 570px; top: 492px; display: flex; gap: 6px; z-index: 5; }
  .slide-dots span { width: 12px; height: 12px; border-radius: 50%; border: 1px solid var(--white); }
  .slide-dots .is-current { background: var(--teal); border-color: var(--teal); }

  .intro { position: absolute; left: 0; top: 554px; width: 1200px; height: 140px; text-align: center; }
  .intro-text { width: 440px; margin: 28px auto 0; font-size: 13px; line-height: 1.6; color: var(--ink); }
  .section-title {
    margin-top: 26px; font-family: "Quicksand", sans-serif; font-size: 18px; font-weight: 500; color: var(--ink);
  }

  .services { position: absolute; left: 0; top: 704px; width: 1200px; height: 85px; background: var(--navy); }
  .service-dot {
    position: absolute; top: -22px; width: 44px; height: 44px; border-radius: 50%;
    background: var(--teal); border: 4px solid var(--navy);
  }
</style>
</head>
<body>
  <header class="site-header">
    <div class="brand">
      <span class="brand-mark"></span>
      <span class="brand-name">Velquant Security</span>
    </div>
    <ul class="main-nav">
      <li class="is-active">Home</li>
      <li>Penetration Testing</li>
      <li>Staffing</li>
      <li>News</li>
      <li>About Us</li>
      <li>Contact Us</li>
    </ul>
  </header>

  <svg class="edge" style="top:80px" viewBox="0 0 1200 10" aria-hidden="true">
    <defs><pattern id="zig-down" width="10" height="10" patternUnits="userSpaceOnUse"><path d="M0 0 L5 8 L10 0 Z" fill="#eeeeee"/></pattern></defs>
    <rect width="1200" height="10" fill="url(#zig-down)"/>
  </svg>

  <section class="hero-top" role="img" aria-label="Faint line icons of security and office objects scattered over the navy background"></section>

  <svg class="edge" style="top:296px" viewBox="0 0 1200 10" aria-hidden="true">
    <defs><pattern id="zig-up" width="10" height="10" patternUnits="userSpaceOnUse"><path d="M0 10 L5 2 L10 10 Z" fill="#e8e8e8"/></pattern></defs>
    <rect width="1200" height="10" fill="url(#zig-up)"/>
  </svg>
  <div class="hero-band"></div>
  <svg class="edge" style="top:422px" viewBox="0 0 1200 10" aria-hidden="true">
    <rect width="1200" height="10" fill="url(#zig-down)" style="fill:url(#zig-down)"/>
  </svg>
  <section class="hero-bottom" role="img" aria-label="Faint line icons continuing across the navy background">
    <div class="rule"></div>
  </section>
  <svg class="edge" style="top:540px" viewBox="0 0 1200 10" aria-hidden="true">
    <rect width="1200" height="10" fill="url(#zig-up)"/>
  </svg>

  <article class="slide-card">
    <h1 class="slide-title">Dedicated to your infosec staffing requirements</h1>
    <div class="slide-divider"></div>
    <p class="slide-text">Velquant Security is a niche company that is devoted to InfoSec resourcing, with qualified, in-house security professionals that talk tech.</p>
    <span class="btn-contact">Contact Us</span>
  </article>
  <div class="slide-arrow prev"><svg width="12" height="12" viewBox="0 0 12 12"><path d="M8 1 L3 6 L8 11" stroke="#1c2e3d" stroke-width="2.4" fill="none"/></svg></div>
  <div class="slide-arrow next"><svg width="12" height="12" viewBox="0 0 12 12"><path d="M4 1 L9 6 L4 11" stroke="#1c2e3d" stroke-width="2.4" fill="none"/></svg></div>
  <div class="slide-dots"><span></span><span class="is-current"></span><span></span></div>

  <section class="intro">
    <p class="intro-text">Donec sollicitudin molestie malesuada. Nulla quis lorem ut libero malesuada feugiat. Curabitur aliquet quam id dui lorem.</p>
    <h2 class="section-title">Our Services</h2>
  </section>

  <section class="services">
    <span class="service-dot" style="left:378px"></span>
    <span class="service-dot" style="left:578px"></span>
    <span class="service-dot" style="left:778px"></span>
  </section>
</body>
</html>
```